Non-Alcoholic Beverage Industry Grant Recipient Signage (Recycling Focus)

Millbrook StreetBloom, a non-profit organization in Youngstown, OH, recently received a grant through the Ohio Drinkmakers Guild (us) and the National Refreshment Trust for a Thriving Nation. This grant will go towards the installation of garbage/recycling receptacles throughout the downtown area including the Pellham Ridge University campus and adjacent neighborhoods and gateways.
Specifically, this will:
a. Replace garbage receptacles with ones compatible with new Loopwise cigarette butt receptacles previously purchased; this will reduce cigarette litter as well as improve cleanliness of downtown area;
b. Convert current trash receptacles into recycling bins. This would allow Youngstown to start a new downtown recycling program.
We are responsible for designing a 12” by 18” sign that reflects our involvement in the project and encourages recycling. We request that you do not copy/paste the above, rather come up with a creative, unique design that reflects the goal of recycling.
Ohio Drinkmakers Guild
ohiodrinkguild.example
Progress Renewed
https://www.progressrenewed.example/plastic/
National Refreshment Trust for a Thriving Nation http://www.refreshmenttrust.example/
Millbrook StreetBloom
http://www.millbrookstreetbloom.example/
The signage must incorporate the two attached logos.
Updates
Deadline is incorrectly displaying as July 7, which was yesterday. We would like submissions by Friday, July 12 at the latest. Thank you!

```html
<!DOCTYPE html>
<html lang="en">
<head>
<meta charset="utf-8">
<title>Downtown Recycling Sign</title>
<link rel="stylesheet" href="https://fonts.googleapis.com/css2?family=Montserrat:wght@400;500;600;700&display=swap">
<style>
  :root {
    --page-bg: #e6e6e6;
    --border-blue: #7aa9c6;
    --mint-light: #f3fdf1;
    --mint: #e3f8df;
    --ink: #222222;
    --green: #2ea52b;
    --leaf-light: #8fd26a;
    --leaf-dark: #3a9d3c;
    --footer-blue: #15618c;
    --white: #ffffff;
    --logo-blue: #1f5a96;
    --logo-slate: #8a9bc1;
  }
  * { box-sizing: border-box; margin: 0; padding: 0; }
  html, body {
    width: 1200px; height: 1200px; overflow: hidden;
    background: var(--page-bg);
    font-family: "Montserrat", Arial, sans-serif;
  }
  .sign {
    position: absolute; left: 220px; top: 35px;
    width: 760px; height: 1130px;
    background: var(--border-blue);
    padding: 17px;
  }
  .sign-body {
    position: relative; width: 726px; height: 1096px; overflow: hidden;
    background: radial-gradient(ellipse at 40% 45%, #ffffff 0%, var(--mint-light) 40%, var(--mint) 100%);
  }
  .partner-bar {
    position: absolute; top: 62px; left: 42px; right: 42px;
    display: flex; justify-content: space-between; align-items: center;
  }
  .partner-mark { display: flex; align-items: center; gap: 10px; }
  .partner-mark .mark-square { width: 28px; height: 28px; background: var(--logo-blue); }
  .partner-mark .mark-name {
    font-weight: 700; font-size: 20px; line-height: 1.15; color: var(--logo-blue); width: 170px;
  }
  .partner-mark.trust .mark-name {
    font-weight: 600; font-size: 20px; color: var(--logo-slate); width: 340px; text-align: right;
  }
  .goal-detail {
    position: absolute; left: 63px; top: 178px;
    font-size: 26px; line-height: 34px; font-weight: 500; color: var(--ink);
    white-space: nowrap;
  }
  .goal-main {
    position: absolute; left: 63px; top: 382px;
    font-size: 30px; line-height: 39px; font-weight: 700; color: var(--ink);
    white-space: nowrap;
  }
  .accent { color: var(--green); font-weight: 700; }
  .goal-main .accent { font-size: 32px; }
  .art {
    position: absolute;
    background: linear-gradient(160deg, var(--leaf-light), var(--leaf-dark));
  }
  .art.leaves { left: 470px; top: 360px; width: 250px; height: 215px; border-radius: 50%; opacity: 0.7; }
  .art.bin { left: 443px; top: 560px; width: 255px; height: 298px; border-radius: 6px 6px 10px 10px; opacity: 0.9; }
  .art.ground { left: 34px; top: 690px; width: 400px; height: 168px; border-radius: 70px 70px 0 0; opacity: 0.55; }
  .credits {
    position: absolute; left: 0; bottom: 0; width: 100%; height: 238px;
    background: var(--footer-blue); color: var(--white);
  }
  .credit { position: absolute; text-align: center; }
  .credit .label { font-size: 16px; line-height: 20px; font-weight: 500; }
  .credit .url {
    margin-top: 6px; height: 31px; border: 1.5px solid var(--white); border-radius: 16px;
    font-size: 15px; line-height: 28px; font-weight: 500; white-space: nowrap;
  }
  .credit.guild { left: 36px; top: 40px; width: 292px; }
  .credit.renewed { left: 352px; top: 40px; width: 338px; }
  .credit.trust { left: 36px; top: 123px; width: 292px; }
  .credit.bloom { left: 352px; top: 143px; width: 338px; }
</style>
</head>
<body>
  <main class="sign">
    <div class="sign-body">
      <header class="partner-bar">
        <div class="partner-mark guild">
          <span class="mark-square"></span>
          <span class="mark-name">Ohio Drinkmakers Guild</span>
        </div>
        <div class="partner-mark trust">
          <span class="mark-name">National Refreshment Trust for a Thriving Nation</span>
        </div>
      </header>

      <p class="goal-detail">
        <span class="accent">Replace garbage</span> receptacles with ones<br>
        compatible with new <span class="accent">Loopwise cigarette</span><br>
        butt receptacles previously purchased;<br>
        this will reduce cigarette litter as well as<br>
        improve cleanliness of <span class="accent">downtown</span> area
      </p>

      <p class="goal-main">
        Convert current <span class="accent">trash</span><br>
        receptacles into<br>
        recycling bins.<br>
        This would allow<br>
        <span class="accent">Youngstown</span> to start<br>
        a new <span class="accent">downtown</span><br>
        <span class="accent">recycling program.</span>
      </p>

      <div class="art leaves" role="img" aria-label="Cluster of fresh green leaves growing out of the recycling bin"></div>
      <div class="art bin" role="img" aria-label="Green recycling bin with white recycle arrows"></div>
      <div class="art ground" role="img" aria-label="Open bin lid resting on the ground among green leaves"></div>

      <footer class="credits">
        <div class="credit guild">
          <p class="label">Ohio Drinkmakers Guild</p>
          <p class="url">www.ohiodrinkguild.example</p>
        </div>
        <div class="credit renewed">
          <p class="label">Progress Renewed</p>
          <p class="url">www.progressrenewed.example/plastic/</p>
        </div>
        <div class="credit trust">
          <p class="label">National Refreshment Trust<br>for a Thriving Nation</p>
          <p class="url">www.refreshmenttrust.example/</p>
        </div>
        <div class="credit bloom">
          <p class="label">Millbrook StreetBloom</p>
          <p class="url">www.millbrookstreetbloom.example/</p>
        </div>
      </footer>
    </div>
  </main>
</body>
</html>
```